Bumblecrest Nursery - Brochure Design Project

Hi,
We would like a beautiful brochure for Bumblecrest Nursery and Day Care in Sharjah, a design that can be later adapted to leaflet and website designs.
The Purpose: The purpose of the brochure is to portray that Bumblecrest is a fun and creative place that helps your child attain an all round development.
The Nursery has exceptional facilities and experienced staff and that is why the brochure should look elegant and attractive, meeting the standards of the Nursery.
We believe that in the long term this brochure will help us to carve a niche as a creative early development centre and one of the most reliable names in this industry.
Target Audience: Our target audience are the young mothers (with children from 6 months – 4 years) who want a safe, reliable and professional place to help give their child an extra edge.
The Idea: We would love to have something that can connect children factor to the Brochure, preferably child like illustrations on the cover and throughout the brochure.
You can use the visual of children but do make sure you portray cute Indian kids more, because they are the ones we will be ultimately targeting.
You can use white, cream or light and bright colours like yellow, orange, rose and sky blue for the brochure.
Though there is no fixed logo at the moment, do put in a good font and design as the Bumblecrest logo.
We have attached two different ads (both are not nursery ads) where we like the treatment and we are looking forward to seeing something like this in terms of art and layout.
In Reference 1: We like the child like illustrations and the way the image of the young girl is placed. We could have visuals of children on the cover and continue with the illustrations throughout the brochure.
In Reference 2: We love the illustrations and the way the copy is placed. We could probably place the headline on the brochure cover in such a manner.
No. of Pages: We would prefer to have a brochure with total 4 pages
Deadline: Since admissions are starting and time is running out, we need the artwork by August 11th.
Copy: Please do send a sample of the brochure artwork you did (preferably cover and one inside page) with dummy copy. We shall provide you with the original copy once the design is selected.
Looking forward to working with you.
Thank you
Regards
Harish Kottaram

```html
<!DOCTYPE html>
<html lang="en">
<head>
<meta charset="utf-8">
<title>Bumblecrest Nursery – Inside Spread</title>
<link rel="stylesheet" href="https://fonts.googleapis.com/css2?family=Gochi+Hand&family=Ubuntu:wght@400&display=swap">
<style>
  :root {
    --backdrop: #2b2b2b;
    --cream: #fbe9da;
    --cream-light: #fffaf5;
    --orange: #f26a1b;
    --yellow: #fdc010;
    --ink: #2d2a26;
    --photo-warm: #e9b38a;
    --photo-light: #f6e8dc;
  }
  * { box-sizing: border-box; margin: 0; padding: 0; }
  html, body { width: 1200px; height: 1000px; overflow: hidden; }
  body { background: var(--backdrop); position: relative; font-family: "Ubuntu", "Tahoma", sans-serif; color: var(--ink); }

  .spread { position: absolute; left: 50px; top: 28px; width: 1108px; height: 784px; display: flex; box-shadow: 0 6px 24px rgba(0,0,0,.6); }
  .page { position: relative; width: 554px; height: 784px; overflow: hidden;
          background: radial-gradient(ellipse at 50% 45%, var(--cream-light) 30%, var(--cream) 100%); }
  .page--right { border-left: 1px solid #d9c6b6; }
  .band { position: absolute; left: 0; top: 0; }

  .heading { position: absolute; font-family: "Gochi Hand", cursive; font-weight: 400; color: var(--orange); font-size: 40px; line-height: 1; }
  .copy { position: absolute; font-size: 12.2px; line-height: 18.6px; white-space: nowrap; }

  .photo { position: absolute; border-radius: 6px; }
  .photo--kids { left: 5px; top: 60px; width: 295px; height: 322px;
    background: radial-gradient(ellipse at 50% 50%, var(--photo-warm) 0%, #d86a4a 40%, var(--photo-light) 80%); opacity: .85; }
  .photo--babies { left: 48px; top: 352px; width: 194px; height: 310px; border-radius: 0;
    background: radial-gradient(ellipse at 50% 50%, #f1cfb6 0%, #c9c9c9 45%, var(--photo-light) 85%); opacity: .9;
    clip-path: polygon(0 0, 125px 0, 125px 36px, 140px 36px, 140px 110px, 174px 110px, 174px 148px, 194px 148px, 194px 310px, 0 310px); }

  .photo-circle { position: absolute; left: 378px; top: 436px; width: 154px; height: 154px; border-radius: 50%;
    background: #fff; border: 4px solid var(--orange); }

  /* page 1 */
  .who-title { left: 310px; top: 30px; }
  .who-copy { left: 312px; top: 71px; }
  .band-copy-1 { left: 37px; top: 412px; }
  .heading-p1 { left: 35px; top: 570px; }
  .cols-p1a { left: 32px; top: 611px; }
  .cols-p1b { left: 292px; top: 611px; }

  /* page 2 */
  .heading-p2a { left: 36px; top: 32px; }
  .cols-p2a { left: 30px; top: 82px; }
  .cols-p2b { left: 286px; top: 82px; }
  .heading-p2b { left: 36px; top: 228px; }
  .wide-copy { left: 30px; top: 277px; }
  .wrap-copy { left: 150px; top: 314px; width: 382px; text-align: center; }
  .band-copy-2 { left: 37px; top: 694px; }
</style>
</head>
<body>
<div class="spread">

  <section class="page page--left">
    <svg class="band" width="554" height="784" viewBox="0 0 554 784" aria-hidden="true">
      <path d="M0,540 C200,532 380,522 554,524 L554,542 C380,544 180,552 0,570 Z" fill="var(--orange)"/>
      <path d="M0,404 C160,392 350,374 554,366 L554,527 C380,526 200,532 0,546 Z" fill="var(--yellow)"/>
    </svg>

    <div class="photo photo--kids" role="img" aria-label="Photo of a group of smiling young children with school backpacks"></div>

    <h2 class="heading who-title">Who we are</h2>
    <p class="copy who-copy">Commod dunt autet, quipit iniam,<br>venit acinim iriuscilisl ute min<br>veliquiscil del ex ent lor se dolore<br>core et praesenis adignibh exerosto<br>er irit, si.<br>Rit augait nullaorperit in velessim<br>eliquip sustis nons aci tie feui tat<br>niamcon sequamet am iure tisit alit<br>dio odolorpero etue dolore minit nim<br>inim iriliqui eu feuguer cidunt at utet<br>amconse estrud molobore et dolorer<br>cidunt il utpat lore velit augiam del<br>ut vulpute erosto odiamcommod ming<br>endit nos adipsum sandit del ing ea<br>faciduisit laore do doluptation<br>eummy nim ilissed erostions ea</p>

    <p class="copy band-copy-1">Commod dunt autet, quipit iniam, venit acinim iriuscilisl ute min<br>veliquiscil del ex ent lor se dolore core et praesenis adignibh<br>exerosto er irit, si. Rit augait nullaorperit in velessim<br>eliquip sustis nons aci tie feui tat niamcon sequamet am<br>iure tisit alit dio odolorpero etue dolore minit nim inim<br>iriliqui eu feuguer cidunt at utet amconse estrud</p>
    <div class="photo-circle" role="img" aria-label="Round photo frame"></div>

    <h2 class="heading heading-p1">Heading</h2>
    <p class="copy cols-p1a">Commod dunt autet, quipit iniam, venit<br>acinim iriuscilisl ute min veliquiscil del<br>ex ent lor se dolore core et praesenis<br>adignibh exerosto er irit, si.<br>Rit augait nullaorperit in velessim<br>eliquip sustis nons aci tie feui tat<br>niamcon sequamet am iure tisit alit dio<br>odolorpero etue dolore minit nim inim</p>
    <p class="copy cols-p1b">iriliqui eu feuguer cidunt at utet<br>amconse estrud molobore et dolorer<br>cidunt il utpat lore velit augiam del ut<br>vulpute erosto odiamcommod ming<br>endit nos adipsum sandit del ing ea<br>faciduisit laore do doluptation eummy<br>nim ilissed erostions ea facilluptat<br>wiscipsusto dolore tat ut accum ver</p>
  </section>

  <section class="page page--right">
    <svg class="band" width="554" height="784" viewBox="0 0 554 784" aria-hidden="true">
      <path d="M0,627 C180,650 380,676 554,684 L554,784 L0,784 Z" fill="var(--orange)"/>
      <path d="M0,645 C180,666 380,686 554,691 L554,784 L0,784 Z" fill="var(--yellow)"/>
    </svg>

    <h2 class="heading heading-p2a">Heading</h2>
    <p class="copy cols-p2a">Commod dunt autet, quipit iniam,<br>venit acinim iriuscilisl ute min veliquis-<br>cil del ex ent lor se dolore core et<br>praesenis adignibh exerosto er irit, si.<br>Rit augait nullaorperit in velessim<br>eliquip sustis nons aci tie feui tat<br>niamcon sequamet am iure tisit alit dio</p>
    <p class="copy cols-p2b">odolorpero etue dolore minit nim inim<br>iriliqui eu feuguer cidunt at utet<br>amconse estrud molobore et dolorer<br>cidunt il utpat lore velit augiam del ut<br>vulpute erosto odiamcommod ming<br>endit nos adipsum sandit del ing ea<br>faciduisit laore do doluptation eummy</p>

    <h2 class="heading heading-p2b">Heading</h2>
    <p class="copy wide-copy">Commod dunt autet, quipit iniam, venit acinim iriuscilisl ute min veliquiscil del ex<br>ent lor se dolore core et praesenis adignibh exerosto er irit, si.</p>
    <div class="photo photo--babies" role="img" aria-label="Photo of babies climbing a small stepladder"></div>
    <p class="copy wrap-copy">Rit augait nullaorperit in velessim eliquip sustis nons aci tie<br>feui tat niamcon sequamet am iure tisit alit dio odolorpero<br>etue dolore minit nim inim iriliqui eu feuguer cidunt at<br>utet amconse estrud molobore et dolorer cidunt il<br>utpat lore velit augiam del ut vulpute erosto odiam-<br>commod ming endit nos adipsum sandit del ing ea<br>faciduisit laore do doluptation eummy nim ilissed<br>erostions ea facilluptat wiscipsusto dolore tat ut<br>accum ver iliquam vercin ute magna facin<br>ulluptat ad et init autpat.<br>Ex esto od doloreros nonsed tismodignim<br>quipsustrud min ulla con utpat. Sit luptat<br>lam, siscidunt aliquis acil inciniat. Um ing<br>euisi. Commod dunt autet, quipit iniam,<br>venit acinim iriuscilisl ute min veliquiscil<br>del ex ent lor se dolore core et praesenis<br>adignibh exerosto er irit, si.<br>Rit augait nullaorperit in velessim eliquip<br>sustis nons aci tie feui tat niamcon</p>

    <p class="copy band-copy-2">Commod dunt autet, quipit iniam, venit acinim iriuscilisl ute min veliquiscil del<br>ex ent lor se dolore core et praesenis adignibh exerosto er irit, si.<br>Rit augait nullaorperit in velessim eliquip sustis nons aci tie feui tat niamcon<br>sequamet am iure tisit alit dio odolorpero etue dolore minit nim inim iriliqui eu</p>
  </section>

</div>
</body>
</html>
```